Finance broker brochure to give to Accountants / Financial Planners to promote my services to them

Produce a brochure - probably A5 size - but whatever looks best and so the text isn't too cramped. I am going to distribute to accountants to tell them about my services I want it to include the following images my profile pic, my Wendlocke logo, the GLBC logo, and relevant images - houses, calculators, happy attractive people. Would like it to look spacious and not too cramped - nicely laid out and easy to read. Maybe bullet points. Please refer to my Facebook Page and website to see what styles I use. www.tallowmere.com.au
https://www.facebook.com/pg/tallowmere.com.au/about/

Thank you

Target Market(s)

Accountants / Financial Planners Professional Advisers

Industry/Entity Type

Financial Service

Font styles to use
Serif

Colors
33a6d7
3176b5
ffffff
9ccb3b

Requirements
Must have
• My logo, My profile image, GLBC Logo , Text - clearly legible, well spaced. Colours compatible with logo . Images relevant to mortgage broking / finance brokers. Homes, happy people talking about finance.
• Clear headings and good colour combinations - that match logo theme
Nice to have
• Perhaps Dot points to set out the text.
Should not have
• Too squashed or hard to read text

```html
<!DOCTYPE html>
<html lang="en">
<head>
<meta charset="utf-8">
<title>Wendlocke – Referral Brochure for Accountants</title>
<link href="https://fonts.googleapis.com/css2?family=Marcellus+SC&family=Open+Sans:wght@400;700&display=swap" rel="stylesheet">
<style>
  :root {
    --backdrop: #e9e6e0;
    --paper: #ffffff;
    --brand-blue: #1a4f9c;
    --heading-blue: #1d55a5;
    --ink: #222222;
    --fold-shade: #ececec;
    --photo-sky: #cfe0ee;
    --photo-house: #e7e5df;
    --photo-shirt: #2c4f8e;
  }
  * { box-sizing: border-box; margin: 0; padding: 0; }
  html, body { width: 1200px; height: 1200px; overflow: hidden; background: var(--backdrop); }
  body { font-family: "Open Sans", sans-serif; color: var(--ink); position: relative; }

  .spread {
    position: absolute; left: 74px; top: 228px; width: 1052px; height: 744px;
    background: var(--paper); box-shadow: 0 4px 14px rgba(0,0,0,.18); overflow: hidden;
  }
  .panel { position: absolute; top: 0; height: 744px; overflow: hidden; }
  .panel--cover { left: 0; width: 254px; }
  .panel--intro { left: 254px; width: 272px; }
  .panel--services { left: 526px; width: 272px; background: linear-gradient(90deg, var(--fold-shade) 0, var(--paper) 36px); }
  .panel--closing { left: 798px; width: 254px; }

  .hero-photo {
    position: absolute; left: 0; top: 0; width: 254px; height: 442px;
    background: linear-gradient(180deg, var(--photo-sky) 0%, var(--photo-house) 45%, var(--photo-shirt) 100%);
  }
  .referral-box {
    position: absolute; left: 0; top: 442px; width: 254px; height: 302px;
    background: var(--brand-blue); color: #fff; padding: 32px 20px 0 35px;
  }
  .referral-box h2 {
    font-family: "Marcellus SC", serif; font-weight: 400; font-size: 15px; line-height: 16px;
    letter-spacing: .3px; margin-bottom: 14px;
  }
  .referral-box p { font-size: 10.6px; line-height: 11.9px; }

  .body-text { position: absolute; font-size: 10.3px; line-height: 11.85px; text-align: justify; }
  .panel--intro .body-text { left: 35px; top: 38px; width: 219px; }
  .panel--services .body-text { left: 18px; top: 43px; width: 218px; }
  .panel--closing .body-text { left: 0; top: 43px; width: 218px; }
  .indent { padding-left: 18px; }

  .section-title {
    font-family: "Marcellus SC", serif; font-weight: 400; color: var(--heading-blue);
    font-size: 20px; line-height: 18.5px; margin-bottom: 15px; text-align: left;
  }
  .service-list { list-style: none; }
  .service-list li { position: relative; padding-left: 18px; }
  .service-list li .num { position: absolute; left: 0; top: 0; }
  .service-list li b { font-weight: 700; }

  .legal { position: absolute; left: 0; width: 218px; font-size: 8px; line-height: 9.2px; text-align: justify; }
  .legal--licence { top: 526px; border-top: 1px solid #999; padding-top: 7px; }
  .legal--general { top: 558px; }

  .contact-box {
    position: absolute; left: 0; top: 638px; width: 254px; height: 70px;
    background: var(--brand-blue); color: #fff; text-align: center; padding-top: 14px;
  }
  .contact-box .cta { font-size: 18px; line-height: 20px; }
  .contact-box .phone { font-size: 18px; line-height: 20px; font-weight: 700; }
</style>
</head>
<body>
<div class="spread">

  <section class="panel panel--cover">
    <div class="hero-photo" role="img" aria-label="Photo of a couple seen from behind, arm in arm, looking at a modern white home"></div>
    <div class="referral-box">
      <h2>What Will Referring<br>to Wendlocke Look<br>Like for You ?</h2>
      <p>Client Satisfaction and business growth By by referring your clients to Wendlocke for their finance needs you are providing a holistic service by assisting them to find financial solutions for their needs. You can be confident that they will be given personalised attention with a high standard of customer care and quality service. By helping resolve your clients finance needs you are consolidating your position as their trusted financial advisor opening your business to further growth and referrals.</p>
    </div>
  </section>

  <section class="panel panel--intro">
    <div class="body-text">
      <h1 class="section-title">What Can We Do<br>For You and<br>Your Clients?</h1>
      <p>We know from our own experience in commerce and business that there are many ups and downs faced by individuals and businesses on a daily basis. We would love to be able to assist you with helping your clients with their finance needs to overcome some of the challenges they may face or assist in achieving their financial goals. Here are some examples of areas where we may be able to add value for you for your client</p>
      <ul class="service-list">
        <li><span class="num">1.</span><b>Cash Flow Is King In SMEs</b> Cash flow is an important part of running any business and can be particularly the case in SMEs. Often businesses are asset rich and cash flow poor, experiencing periods of time when things are overly tight due to timing differences such as delays in debtor payments or subtle changes in market conditions that are cyclical - like traditionally quiet times of the year. As their Accountant you may be able to assist your client by referring them to Wendlocke who could assist your client to get cash out for business purposes and so relieve short-term financial stress.</li>
        <li><span class="num">2.</span><b>Tax Debt Refinancing</b> Once the legislation is adopted the ATO will have authority to report to credit reporting bureaus (CRBs) business tax debts over $10,000, that are over 90 days overdue and where the business hasn't engaged with the ATO effectively to manage the tax debt. This could affect businesses' credit records which could impact on their capacity to borrow funds in the future or negatively affect creditor / supplier terms. Wendlocke can assist your clients with refinancing tax debts to avoid having the debt negatively impact your client's credit record.</li>
        <li><span class="num">3.</span><b>Consolidating Multiple Personal Debts</b> - With credit cards readily accessible and the costs of living rising it is not uncommon to see clients facing financial stress with credit card debt that gets out of hand for one reason or another. Interest rates on credit cards</li>
      </ul>
    </div>
  </section>

  <section class="panel panel--services">
    <div class="body-text">
      <p class="indent">when not paid off in full can be up to 21 % pa. To help your client get out of that situation a sensible strategy may be to refinance and consolidate the cards and other higher rate loans like personal loans and amalgamate them with their owner occupied loan or consolidate in to a lower rate personal loan. By doing this the rate of interest that your client may experience could drop from 21% to under 4% on the same debts. Of course this would be done under your financial guidance and expertise with the recommendation for the client to close the cards to prevent finding themselves in the same situation in the future.</p>
      <ul class="service-list">
        <li><span class="num">4.</span><b>Save Money on the Home loan through Refinancing</b>. Your clients go through various ups and downs and stages depending on their financial situation and family circumstances. It is not uncommon for a couple with a family to find themselves short on cash due to ill health, education costs or having had a period of under employment or relationship breakdown. Refinancing the owner occupied loan can enable the client to reduce their mortgage costs and if need be access some of the equity in their home that may have come through property price increases or through reducing repayments by lowering the interest rate. They may also be able to restructure their loan to better suit their circumstances.<br>It makes sense to look at refinancing review the home loan every 3 to 5 years. Banks generally are not as generous to their existing clients with rate discounts as they are when trying to attract new clients and so interest good savings can may be achieved by simply refinancing and taking advantage of lower rates - putting more money in your clients pocket now. This can allow your client to put the extra savings towards paying down non-deductible debt quicker.</li>
        <li><span class="num">5.</span><b>Wealth Creation – Investment</b>. If your clients want to grow their wealth and work towards securing their financial future they may be interested in establishing or have already established their own SMSF. We can</li>
      </ul>
    </div>
  </section>

  <section class="panel panel--closing">
    <div class="body-text">
      <p class="indent">assist your client with finance for their SMSF investments or personal investments. As a finance broker we are able to look at your clients financial goals and work with you to help them to achieve their investment objectives. We are able to source SMSF loans and assist with investment lending . It is particularly relevant in today's tightening finance climate to use an experienced finance professional like Wendlocke to guide the client and yourself through the constantly changing financial landscape.</p>
      <ul class="service-list">
        <li><span class="num">6.</span><b>Commercial Loans</b>. Your business clients may be in a growth phase where they require bigger premises or new equipment to enable their business to grow. At Wendlocke we have access to a number of commercial lenders that may be able to assist your clients. We can work with you to review what your client requires and to select the most appropriate lender for your client and put the loan together for submission to the lender. By doing this you have added value for your client and enabled them to grow in their business.</li>
        <li><span class="num">7.</span><b>Asset Finance</b> - If your client is in construction and needs some new “yellow goods”, trucks, or machinery for other business purposes or simply a new vehicle for personal use Wendlocke is able to provide competitive finance options for your clients. It is recommended to get a few finance quotes when doing asset finance and make sure that you are comparing “like with like” when looking at various options.</li>
      </ul>
    </div>
    <p class="legal legal--licence">Credit Representative 517204 is authorised under Australian Credit Licence 402611</p>
    <p class="legal legal--general">This provides general information only and has been prepared without taking into account individual objectives, financial situation or needs. The full financial situation will need to be reviewed prior to acceptance of any offer or product. Subject to lenders terms and conditions, fees and charges and eligibility criteria apply.</p>
    <div class="contact-box">
      <div class="cta">CONTACT US NOW!</div>
      <div class="phone">1300 55 42 10</div>
    </div>
  </section>

</div>
</body>
</html>
```